House Builder and Property Development Card Design and Logo

I need a business card design for a building and property development company.
Colour scheme of Dark Grey and Green, I would like it bold, sharp and professional.
No logo yet done, I'm open to options but please stay away from the usual- house, roof, hammers etc.
Thanks Rob

Please be aware that on the business card information section the WHRC # 5528391 is a licence number and my phone number 0492837165. The numbers are close together and could be mistaken as one whole number 

Thank you

                                   

Industry/Entity Type

Building

Contact Information for Business Card

VARGA BUILD & DEVELOPMENT.
Residential Building & Property Development
Robert Varga - Director
WHRC # 5528391
0492837165
rob@vargabuild.example.com.au

Requirements
Must have
• Bold Business name
Dark grey and green colours
Should not have
• roof outline or hammer logo

```html
<!DOCTYPE html>
<html lang="en">
<head>
<meta charset="utf-8">
<title>Varga Build &amp; Development – Business Card</title>
<link rel="stylesheet" href="https://fonts.googleapis.com/css2?family=Mulish:ital,wght@0,400;0,800;1,400&family=Italianno&display=swap">
<style>
  :root {
    --card-bg: #ffffff;
    --brand-green: #6fa843;
    --brand-grey: #4a4a4c;
    --band-grey: #4d4d4f;
    --band-text: #f2f2f2;
    --script-grey: #4f4f4f;
  }
  * { margin: 0; padding: 0; box-sizing: border-box; }
  html, body { width: 1200px; height: 742px; overflow: hidden; background: var(--card-bg); }
  .card {
    position: relative;
    width: 1200px;
    height: 742px;
    background: var(--card-bg);
    font-family: "Mulish", "Century Gothic", sans-serif;
  }
  .contact-name {
    position: absolute;
    right: 104px;
    top: 82px;
    font-size: 46px;
    font-weight: 400;
    color: var(--brand-green);
    letter-spacing: 0.5px;
    line-height: 1;
  }
  .contact-role {
    position: absolute;
    right: 116px;
    top: 130px;
    font-family: "Italianno", cursive;
    font-size: 46px;
    color: var(--script-grey);
    line-height: 1;
  }
  .brand-mark {
    position: absolute;
    left: 95px;
    top: 365px;
    width: 180px;
    height: 180px;
    background: var(--brand-green);
  }
  .brand-name {
    position: absolute;
    right: 77px;
    top: 484px;
    font-size: 52px;
    font-weight: 800;
    color: var(--brand-grey);
    line-height: 1;
    letter-spacing: -0.5px;
    white-space: nowrap;
  }
  .brand-rule {
    position: absolute;
    left: 73px;
    top: 549px;
    width: 1050px;
    height: 4px;
    background: var(--brand-green);
  }
  .tagline {
    position: absolute;
    left: 0;
    right: 0;
    top: 562px;
    text-align: center;
    font-family: "Italianno", cursive;
    font-size: 56px;
    color: var(--script-grey);
    line-height: 1;
    letter-spacing: 1px;
  }
  .info-band {
    position: absolute;
    left: 73px;
    top: 631px;
    width: 1050px;
    height: 56px;
    background: var(--band-grey);
    color: var(--band-text);
    display: flex;
    align-items: center;
    justify-content: space-between;
    padding: 0 22px;
    font-size: 29px;
    font-style: italic;
    letter-spacing: 0.5px;
  }
  .licence-phone { display: flex; gap: 16px; }
</style>
</head>
<body>
  <div class="card">
    <div class="contact-name">Robert Varga</div>
    <div class="contact-role">Director</div>

    <span class="brand-mark"></span>
    <div class="brand-name">Varga Build &amp; Development</div>
    <div class="brand-rule"></div>

    <div class="tagline">Residential Building &amp; Property Development</div>

    <div class="info-band">
      <span class="licence-phone">
        <span class="licence">WHRC # 5528391</span>
        <span class="phone">0492837165</span>
      </span>
      <span class="email">rob@vargabuild.example.com.au</span>
    </div>
  </div>
</body>
</html>
```